New Advertising Company Business Card

A two sided business card. One side with logo only and the other side with my information and maybe my logo again. Looking for something unique and creative, but not too busy. Info would include my name(Marcus Feldon), President, phone number, address, email address, and website. LOGO IS THE BLUE AND WHITE ONE.

Target Market(s)

CEO/VP Level Audience

Industry/Entity Type

Business

Contact Information for Business Card

In Description.

```html
<!DOCTYPE html>
<html lang="en">
<head>
<meta charset="utf-8">
<title>Crestline Advertising – Business Card</title>
<link rel="stylesheet" href="https://fonts.googleapis.com/css2?family=Montserrat:wght@400;600;700&display=swap">
<style>
  :root {
    --page-bg: #ecebe8;
    --card-white: #ffffff;
    --card-dark: #222222;
    --brand-blue: #1072b8;
    --ink: #222222;
    --ink-soft: #3a3a3a;
    --light-text: #ffffff;
  }
  * { box-sizing: border-box; margin: 0; padding: 0; }
  html, body {
    width: 1200px; height: 1000px; overflow: hidden;
    background: var(--page-bg);
    font-family: "Montserrat", Arial, sans-serif;
  }
  .canvas { position: relative; width: 1200px; height: 1000px; }

  .card {
    position: absolute; left: 255px; width: 665px; height: 380px;
    border-radius: 22px; overflow: hidden;
  }
  .card--front { top: 100px; background: var(--card-white); }
  .card--back { top: 520px; background: var(--card-dark); }

  .card__bands { position: absolute; left: 0; bottom: 0; width: 665px; height: 32px; }

  .wordmark {
    position: absolute; color: var(--brand-blue);
    font-weight: 600; letter-spacing: 0.12em; text-align: center; line-height: 1.15;
  }
  .card--front .wordmark { left: 65px; top: 150px; width: 260px; font-size: 29px; }
  .card--back .wordmark { left: 0; top: 118px; width: 665px; font-size: 38px; }
  .wordmark__dot {
    display: block; margin: 0 auto 12px; width: 18px; height: 18px;
    border-radius: 50%; background: var(--brand-blue);
  }

  .divider {
    position: absolute; left: 342px; top: 100px; width: 2px; height: 180px;
    background: var(--brand-blue);
  }

  .contact { position: absolute; left: 379px; top: 96px; color: var(--ink-soft); }
  .contact__name {
    font-size: 26px; font-weight: 700; color: var(--brand-blue);
    letter-spacing: 0.01em; line-height: 1;
  }
  .contact__role { font-size: 15px; margin-top: 6px; }
  .contact__address { font-size: 15px; line-height: 22px; margin-top: 16px; }
  .contact__list { list-style: none; margin-top: 14px; font-size: 15px; }
  .contact__item { display: flex; align-items: center; height: 21px; }
  .contact__icon { width: 10px; height: 10px; margin-right: 10px; fill: var(--brand-blue); }

  .card__web {
    position: absolute; left: 0; bottom: 26px; width: 665px; text-align: center;
    color: var(--light-text); font-size: 15px; letter-spacing: 0.06em;
  }
  .card__web-accent { color: var(--brand-blue); }
</style>
</head>
<body>
<main class="canvas">

  <section class="card card--front" aria-label="Business card, information side">
    <div class="wordmark"><span class="wordmark__dot"></span>CRESTLINE<br>ADVERTISING</div>
    <div class="divider"></div>
    <div class="contact">
      <h1 class="contact__name">MARCUS FELDON</h1>
      <p class="contact__role">Founder</p>
      <p class="contact__address">2480 Coral Ridge Ave.<br>Lantana Shores, FL 33410</p>
      <ul class="contact__list">
        <li class="contact__item">
          <svg class="contact__icon" viewBox="0 0 10 10" aria-hidden="true"><path d="M2 0.5 L3.6 2.6 L2.6 3.6 Q3.6 6 6.4 7.4 L7.4 6.4 L9.5 8 L8.2 9.5 Q2 9 0.5 1.8 Z"/></svg>
          954-555-0148
        </li>
        <li class="contact__item">
          <svg class="contact__icon" viewBox="0 0 10 10" aria-hidden="true"><path d="M0.5 2 H9.5 V8 H0.5 Z M1.4 2.8 V7.2 H8.6 V2.8 L5 5.4 Z" fill-rule="evenodd"/></svg>
          marcus@feldonadstudio.com
        </li>
        <li class="contact__item">
          <svg class="contact__icon" viewBox="0 0 10 10" aria-hidden="true"><circle cx="5" cy="5" r="4.3" fill="none" stroke="#1072b8" stroke-width="1"/><path d="M0.7 5 H9.3 M5 0.7 Q2.5 5 5 9.3 M5 0.7 Q7.5 5 5 9.3" fill="none" stroke="#1072b8" stroke-width="0.8"/></svg>
          www.FeldonAdStudio.com
        </li>
      </ul>
    </div>
    <svg class="card__bands" viewBox="0 0 665 32" aria-hidden="true">
      <rect class="band band--dark" x="0" y="18" width="340" height="14" fill="#222222"/>
      <polygon class="band band--blue" points="370,2 665,2 665,32 335,32" fill="#1072b8"/>
    </svg>
  </section>

  <section class="card card--back" aria-label="Business card, brand side">
    <div class="wordmark"><span class="wordmark__dot"></span>CRESTLINE<br>ADVERTISING</div>
    <p class="card__web">www.<span class="card__web-accent">yourwebsite</span>.com</p>
  </section>

</main>
</body>
</html>
```